We are looking for a 2-page (front and back) 3.67" x 8.5" rack card. . Please refer back to our other Rack Cards for a similar look and feel to the card. This one is titled: Myths and Truths About Memory Loss
The document is for older readers. Do not put text over graphics and keep it simple and easy to read with high contrast.
We want some very simple design element(s) incorporated that convey Native American communities or heritage. But NO headdress, teepee graphics, owls etc. I have included some graphics, please use your creative discretion to use which ones look good on the cards. Please remember to include the funding statement - it can be in a very small font 6/7 point. For more information about our project, please visit https://orvelmesa.net/mind-care/library - This rack card is supported by the Bureau for Wellness Tracking and Outreach (BWT) of the Federal Office of Family and Care Affairs (FOF) as part of a financial assistance award totaling $1,053,119.36 with 100 percent funded by BWT/FOF. The contents are those of the author(s) and do not necessarily represent the official views of, nor an endorsement, by BWT/FOF, or the U.S. Government.
Please feel free to choose one of each of the 2 logos that looks best. We have the QT7 logo and the Mind Wellness Support Hub logo we would like to add. I have added the document and there are images to choose from to use in the rack card. We definitely want to incorporate the coyote in this rack card since it is culturally significant.

```html
<!DOCTYPE html>
<html lang="en">
<head>
<meta charset="utf-8">
<title>Myths and Truths About Memory Loss – Rack Card</title>
<link href="https://fonts.googleapis.com/css2?family=Bebas+Neue&family=Poppins:ital,wght@0,400;0,500;0,600;0,700;1,400&family=Open+Sans:wght@400&display=swap" rel="stylesheet">
<style>
:root{
  --bg:#a3a1a2;
  --paper:#ffffff;
  --maroon:#6b2d29;
  --maroon-deep:#3a1515;
  --teal:#245c5f;
  --teal-light:#4ea7ae;
  --myth-label:#52b6c2;
  --truth-label:#dd7a6f;
  --ink:#2a1010;
}
*{margin:0;padding:0;box-sizing:border-box}
html,body{width:1034px;height:1200px;overflow:hidden;background:var(--bg)}
.stage{position:absolute;left:0;top:0;width:1500px;height:1741px;transform:scale(0.6893);transform-origin:0 0;font-family:'Poppins',sans-serif}
.card{position:absolute;top:186px;width:590px;height:1369px;background:var(--paper);overflow:hidden;box-shadow:0 14px 30px rgba(0,0,0,.25)}
.card--front{left:124px}
.card--back{left:802px}
.abs{position:absolute}

.brand{left:42px;top:52px;display:flex;align-items:center;gap:8px}
.brand-dot{width:18px;height:18px;border-radius:50%;background:var(--maroon)}
.brand-name{font-weight:700;font-size:40px;color:var(--teal);letter-spacing:1px}
.brand-sub{left:40px;top:112px;width:120px;font-weight:600;font-size:9px;line-height:1.2;color:var(--maroon);text-transform:uppercase}

.title{left:176px;top:42px;width:380px;font-family:'Bebas Neue',sans-serif;font-weight:400;font-size:57px;line-height:49px;letter-spacing:1px;white-space:nowrap}
.title .l1{color:var(--maroon);display:block}
.title .l2{color:var(--teal);display:block}

.intro{left:0;top:172px;width:331px;height:176px;background:var(--maroon);border-radius:0 10px 10px 0;color:#fff;font-size:13.4px;line-height:16.1px;padding:15px 18px 0 42px}
.photo{border-radius:12px;border:2px solid #fff;box-shadow:0 0 0 1.5px var(--teal)}

.vs-head{display:flex;align-items:center;gap:12px}
.vs-box{width:172px;height:44px;color:#fff;font-weight:600;font-size:31px;display:flex;align-items:center;justify-content:center;letter-spacing:1px}
.vs-box.myth{background:var(--teal)}
.vs-box.truth{background:var(--maroon)}
.vs-word{font-weight:700;font-style:italic;font-size:46px;color:var(--maroon)}

.panel{background:var(--maroon-deep);border-radius:14px;color:#fff}
.panel .divider{position:absolute;width:1px;background:#cfb8b5}
.item{position:absolute;font-size:13.6px;line-height:16px}
.item b{display:block;font-weight:700;font-size:17.5px;line-height:20px;letter-spacing:.3px}
.item.m b{color:var(--myth-label)}
.item.t b{color:var(--truth-label)}

.quote{left:62px;top:852px;width:476px;text-align:center;color:var(--ink);font-size:22.5px;line-height:27px}
.qmark{position:absolute;font-family:Georgia,serif;font-weight:700;font-size:42px;color:var(--teal);line-height:1}
.quote-by{left:0;top:944px;width:590px;text-align:center;font-weight:700;font-size:23px;color:var(--maroon-deep)}
.quote-src{left:0;top:977px;width:590px;text-align:center;font-style:italic;font-size:16px;color:var(--ink)}

.band{left:0;width:590px;background:var(--teal)}
.band-light{background:var(--teal-light)}
.site{left:0;width:590px;text-align:center;color:#fff;font-weight:600;font-size:33px;letter-spacing:3px}

.h2{left:0;width:590px;text-align:center;font-weight:700;color:var(--maroon-deep)}
.body{left:40px;width:512px;text-align:center;font-size:18.2px;line-height:21.5px;color:var(--ink)}
.pill{height:26px;border-radius:13px;background:var(--teal);color:#fff;font-family:'Open Sans',sans-serif;font-size:12px;display:flex;align-items:center;justify-content:center}
.funding{left:43px;top:1241px;width:515px;color:#fff;font-family:'Open Sans',sans-serif;font-size:12px;line-height:16.2px}
</style>
</head>
<body>
<div class="stage">

  <!-- FRONT -->
  <section class="card card--front">
    <div class="abs brand"><span class="brand-dot"></span><span class="brand-name">QT7</span></div>
    <div class="abs brand-sub">Council for Native Elder Wellness</div>
    <h1 class="abs title"><span class="l1">MYTHS AND TRUTHS</span><span class="l2">ABOUT MEMORY LOSS</span></h1>

    <p class="abs intro">People sometimes believe things about memory loss that are not true. Misunderstandings can make it harder for Elders in Native communities to get the help they need when they start having memory issues. Below are some common myths and truths about memory loss, Alzheimer's disease, and related dementias.</p>
    <div class="abs photo" role="img" aria-label="Photo of two smiling Elders standing together outdoors" style="left:338px;top:172px;width:217px;height:178px;background:linear-gradient(160deg,#4f6a3c,#6f6a55 55%,#3f5e8c)"></div>

    <div class="abs vs-head" style="left:72px;top:385px">
      <div class="vs-box myth">MYTH</div><span class="vs-word">VS.</span><div class="vs-box truth">TRUTH</div>
    </div>

    <div class="abs panel" style="left:42px;top:463px;width:506px;height:338px">
      <div class="divider" style="left:252px;top:32px;height:268px"></div>
      <div class="item m" style="left:33px;top:34px;width:200px"><b>MYTH</b>Getting Alzheimer's is a normal part of aging.</div>
      <div class="item t" style="left:267px;top:27px;width:225px"><b>TRUTH</b>It is a disease that not everyone will get.</div>
      <div class="item m" style="left:33px;top:112px;width:200px"><b>MYTH</b>Memory problems and forgetfulness are definite signs of dementia.</div>
      <div class="item t" style="left:267px;top:105px;width:230px"><b>TRUTH</b>Memory problems do not solely determine if they are dementia. Other medical conditions can cause memory problems. Talk to your doctor.</div>
      <div class="item m" style="left:33px;top:224px;width:200px"><b>MYTH</b>Only older people can get Alzheimer's disease.</div>
      <div class="item t" style="left:267px;top:220px;width:225px"><b>TRUTH</b>There have been cases for people as young as twenty-five, though it is rare to undergo treatment.</div>
    </div>

    <span class="qmark" style="left:34px;top:842px">&ldquo;</span>
    <p class="abs quote">The beauty in life is each day is a new day to try again and be a better version of myself than yesterday.</p>
    <span class="qmark" style="left:442px;top:912px">&rdquo;</span>
    <p class="abs quote-by">Lena Harwood (Blackfeet)</p>
    <p class="abs quote-src">personal communication with the author.</p>

    <div class="abs band" style="top:1205px;height:164px"></div>
    <div class="abs photo" role="img" aria-label="Photo of four Elder women seated in a circle outdoors" style="left:40px;top:1040px;width:250px;height:196px;background:linear-gradient(170deg,#b7a98a,#8a6d52 60%,#5d4a3a)"></div>
    <div class="abs photo" role="img" aria-label="Photo of an Elder woman in a white dress seated by a wall" style="left:303px;top:1040px;width:250px;height:196px;background:linear-gradient(100deg,#8b7c6d,#b9aa99 50%,#4f4640)"></div>
    <p class="abs site" style="top:1262px">www.orvelmesa.net</p>
  </section>

  <!-- BACK -->
  <section class="card card--back">
    <div class="abs vs-head" style="left:77px;top:50px">
      <div class="vs-box myth">MYTH</div><span class="vs-word">VS.</span><div class="vs-box truth">TRUTH</div>
    </div>

    <div class="abs panel" style="left:42px;top:108px;width:506px;height:370px">
      <div class="divider" style="left:252px;top:28px;height:314px"></div>
      <div class="item m" style="left:33px;top:33px;width:205px"><b>MYTH</b>People with Alzheimer's disease cannot be happy.</div>
      <div class="item t" style="left:267px;top:27px;width:225px"><b>TRUTH</b>A person with memory loss can experience strong moods and emotions but still enjoy life and relationships.</div>
      <div class="item m" style="left:33px;top:129px;width:205px"><b>MYTH</b>Dementia can be prevented by a certain supplement or food.</div>
      <div class="item t" style="left:267px;top:123px;width:225px"><b>TRUTH</b>Healthy eating may help overall wellness, including brain health. No additional supplements will completely prevent the onset of dementia.</div>
      <div class="item m" style="left:33px;top:241px;width:205px"><b>MYTH</b>Alzheimer's is reversible through prescription drugs.</div>
      <div class="item t" style="left:267px;top:238px;width:225px"><b>TRUTH</b>There are prescription drugs to address symptoms of Alzheimer's and dementia, but there are no medicines that can reverse them.</div>
    </div>

    <h2 class="abs h2" style="top:508px;font-size:24px">What You Can Do</h2>
    <p class="abs body" style="top:545px">If you or someone you love is having memory problems, do not wait. Talk to a healthy provider you trust. Learning the truth can help keep our Elders strong<br>and supported.</p>

    <h2 class="abs h2" style="top:641px;font-size:24.5px">For More Myth-Busting Information</h2>
    <p class="abs body" style="top:678px;font-size:19.5px;line-height:25px;font-weight:500">12 Common Alzheimer's Disease<br>Myths on <b>Kindrel.com</b></p>
    <div class="abs pill" style="left:91px;top:748px;width:414px">https://www.kindrel.com/c/memory-myths-busted/</div>

    <h2 class="abs h2" style="top:790px;font-size:24.5px;line-height:30px">Memory Care Alliance<br>Myths vs. Facts</h2>
    <div class="abs pill" style="left:16px;top:864px;width:565px">https://www.memorycarealliance.org/dementia/research-and-progress/myths-vs-facts</div>

    <h2 class="abs h2" style="top:906px;font-size:24.5px">QT7 Brain Health Resources</h2>
    <div class="abs pill" style="left:140px;top:950px;width:316px">https://orvelmesa.net/resources/</div>

    <div class="abs band band-light" style="top:1167px;height:66px"></div>
    <div class="abs band" style="top:1232px;height:137px"></div>
    <div class="abs photo" role="img" aria-label="Photo of a coyote standing in dry grass" style="left:43px;top:1013px;width:250px;height:168px;background:linear-gradient(120deg,#c9bba3,#a89680 50%,#d8cdb9)"></div>
    <div class="abs photo" role="img" aria-label="Photo of colorful ears of heirloom corn" style="left:300px;top:1013px;width:250px;height:168px;background:linear-gradient(90deg,#c99a3a,#6a1f2c 30%,#8a3a44 55%,#b58e45 80%,#5a2330)"></div>
    <p class="abs site" style="top:1181px">www.orvelmesa.net</p>

    <p class="abs funding">For more information about our project, please visit https://orvelmesa.net/mind-care/library - This rack card is supported by the Bureau for Wellness Tracking and Outreach (BWT) of the Federal Office of Family and Care Affairs (FOF) as part of a financial assistance award totaling $1,053,119.36 with 100 percent funded by BWT/FOF. The contents are those of the author(s) and do not necessarily represent the official views of, nor an endorsement, by BWT/FOF, or the U.S. Government.</p>
  </section>

</div>
</body>
</html>
```